Veranaxis Business Card and Letter Head

We are a leadership assessment consultancy based in Sydney, Australia. We help executive-level decison-makers select leaders for more senior level roles in corporate and government organisations. Our methodology is based on the latest research from the field of neuroscience.
We need a business card design and matching letter head that presents our company, Veranaxis, as a:
1. trusted adviser to senior executive-level decison makers
2. niche consultancy who are experts in the field of assessing leadership talent
3. results-focused solution provider who balance scientific methods with pragmatic solutions
The following company details should be used in all designs:
Company Name: Veranaxis
Details (for business card):
Daniel Prescott
Senior Talent Advisor
Level 29, Brenning Tower
7 Brenning Square
Sydney, NSW 2000 Australia
Phone: 1300 482 716
Mobile: 0412 573 208
Email: daniel.prescott@veranaxis.com.au
Website: veranaxis.com.au
I have attached the logo for Veranaxis (for both a white and black background) - your business card and letter head designs must incoporate this logo and colour scheme.
Thanks for your interest in this project, I'm looking forward to receiving your ideas.
Regards,
Daniel
Executive-level decison-makers in corporate and government organisations (e.g., CEO, VP, Head of Human Resources)
Leadership

```html
<!DOCTYPE html>
<html lang="en">
<head>
<meta charset="utf-8">
<title>Veranaxis Stationery</title>
<link rel="stylesheet" href="https://fonts.googleapis.com/css2?family=Questrial&display=swap">
<style>
  :root {
    --ink: #1a1a1a;
    --brand-red: #c0160c;
    --soft-red: #fbecea;
    --corner-grey: #f2f2f2;
    --paper: #ffffff;
    --backdrop: #ffffff;
  }
  * { margin: 0; padding: 0; box-sizing: border-box; }
  html, body {
    width: 900px; height: 1200px; overflow: hidden;
    background: var(--backdrop);
    font-family: "Questrial", "Helvetica Neue", Arial, sans-serif;
    color: var(--ink);
  }
  .canvas { position: relative; width: 900px; height: 1200px; }

  .letterhead {
    position: absolute; left: 34px; top: 64px; width: 744px; height: 1052px;
    background: var(--paper);
    box-shadow: 0 3px 8px rgba(0,0,0,0.22);
    overflow: hidden;
  }
  .business-card {
    position: absolute; left: 516px; top: 538px; width: 350px; height: 214px;
    background: var(--paper);
    box-shadow: 0 3px 8px rgba(0,0,0,0.25);
    overflow: hidden;
  }

  .wordmark {
    position: absolute; display: flex; align-items: center;
    color: var(--ink); letter-spacing: -0.5px; line-height: 1;
  }
  .wordmark .mark-square { background: var(--brand-red); display: block; flex: none; }
  .letterhead .wordmark { left: 36px; top: 38px; font-size: 36px; gap: 12px; }
  .letterhead .mark-square { width: 24px; height: 24px; }
  .business-card .wordmark { left: 20px; top: 18px; font-size: 22px; gap: 8px; }
  .business-card .mark-square { width: 15px; height: 15px; }

  .corner-mark { position: absolute; right: 0; top: 0; }

  .contact {
    position: absolute; font-style: normal;
    border-left: 1px solid var(--brand-red);
    font-size: 7.5px; line-height: 10px; white-space: nowrap;
  }
  .contact p + p { margin-top: 4px; }
  .letterhead .contact { left: 569px; top: 33px; padding: 2px 0 4px 8px; }
  .business-card .contact { left: 175px; top: 118px; padding: 2px 0 3px 8px; }

  .holder { position: absolute; left: 183px; top: 73px; white-space: nowrap; }
  .holder-name { font-size: 11px; line-height: 14px; }
  .holder-role { font-size: 7.5px; line-height: 10px; margin-top: 1px; }

  .motif-area {
    position: absolute; left: 0; top: 600px; width: 470px; height: 420px;
    background: linear-gradient(160deg, rgba(251,236,234,0) 0%, var(--soft-red) 45%, rgba(251,236,234,0.4) 100%);
  }
  .card-motif-area {
    position: absolute; left: 0; top: 112px; width: 118px; height: 102px;
    background: linear-gradient(135deg, rgba(192,22,12,0.15), var(--brand-red));
  }
</style>
</head>
<body>
<main class="canvas">

  <section class="letterhead" aria-label="Letterhead">
    <div class="wordmark"><span class="mark-square"></span><span>Veranaxis</span></div>

    <svg class="corner-mark" width="62" height="64" viewBox="0 0 62 64" aria-hidden="true">
      <path d="M0 0H30V32H62V64H0Z" fill="var(--corner-grey)"/>
    </svg>

    <address class="contact">
      <p>Level 29, Brenning Tower<br>7 Brenning Square<br>Sydney NSW 2000 Australia</p>
      <p>P: 1300 482 716<br>M: 0412 573 208</p>
      <p>E: daniel.prescott@veranaxis.com.au<br>W: veranaxis.com.au</p>
    </address>

    <div class="motif-area" role="img" aria-label="Faint brand motif decoration"></div>
  </section>

  <section class="business-card" aria-label="Business card">
    <div class="wordmark"><span class="mark-square"></span><span>Veranaxis</span></div>

    <svg class="corner-mark" width="34" height="38" viewBox="0 0 34 38" aria-hidden="true">
      <path d="M0 0H14V22H34V38H0Z" fill="var(--ink)"/>
    </svg>

    <div class="holder">
      <p class="holder-name">Daniel Prescott</p>
      <p class="holder-role">Senior Talent Advisor</p>
    </div>

    <address class="contact">
      <p>Level 29, Brenning Tower<br>7 Brenning Square<br>Sydney NSW 2000 Australia</p>
      <p>P: 1300 482 716<br>M: 0412 573 208</p>
      <p>E: daniel.prescott@veranaxis.com.au<br>W: veranaxis.com.au</p>
    </address>

    <div class="card-motif-area" role="img" aria-label="Red brand motif decoration"></div>
  </section>

</main>
</body>
</html>
```